Amber Meadow LLC business card

I help with the Marketing and Sales of various Natural, Organic, Eco Friendly and Healthy Main Stream products to Retail Corporate accounts as well as Independents and Distributors.I also highlight Private label items to these same Retail Corporate accounts.Cherish the Moments, Enjoy Life!

Speciality & Health Sales and Marketing

Target Market(s)

Men and Women

Industry/Entity Type

Business

Contact Information for Business Card

Amber Meadow, LLC
Lydia Rose Vandermeer
427 West Orchard Lane
Ste 5-384
Phoenix, AZ 85317
602-718-3054
lvandermeer@pinemail.net

Requirements
Must have
• Nice, femine font
Something in the background or on a side with a softness
Nice to have
• Cherish the Moments, Enjoy Life
Should not have
• Hardness

```html
<!DOCTYPE html>
<html lang="en">
<head>
<meta charset="utf-8">
<title>Amber Meadow LLC – Business Card</title>
<link rel="stylesheet" href="https://fonts.googleapis.com/css2?family=Great+Vibes&family=Roboto+Condensed:wght@400&display=swap">
<style>
  :root {
    --stage: #1c1c1e;
    --magenta: #e2007a;
    --white: #ffffff;
    --mist-blue: #d8ecf2;
    --mist-green: #b9d9a6;
    --leaf-green: #8fc27a;
    --blossom: #f2a9c8;
    --hair: #8a5a3c;
    --skin: #e9c2a6;
  }
  * { box-sizing: border-box; margin: 0; padding: 0; }
  html, body {
    width: 1200px;
    height: 858px;
    overflow: hidden;
    background: var(--stage);
  }
  .card {
    position: absolute;
    left: 56px;
    top: 110px;
    width: 1088px;
    height: 638px;
    border-radius: 24px;
    overflow: hidden;
    background: var(--white);
  }
  .card__photo {
    position: absolute;
    left: 0;
    top: 0;
    width: 100%;
    height: 470px;
    background:
      radial-gradient(ellipse 170px 250px at 150px 210px, var(--skin) 0%, rgba(233,194,166,0.6) 45%, rgba(138,90,60,0.0) 100%),
      radial-gradient(ellipse 260px 360px at 110px 260px, var(--hair) 0%, rgba(138,90,60,0.55) 55%, rgba(138,90,60,0) 100%),
      radial-gradient(circle 70px at 980px 250px, rgba(242,169,200,0.7), rgba(242,169,200,0) 100%),
      radial-gradient(circle 60px at 960px 420px, rgba(242,169,200,0.6), rgba(242,169,200,0) 100%),
      radial-gradient(ellipse 380px 260px at 760px 360px, var(--leaf-green), rgba(143,194,122,0) 100%),
      linear-gradient(160deg, var(--mist-blue) 0%, #eef5ef 40%, var(--mist-green) 100%);
  }
  .card__title {
    position: absolute;
    font-family: "Great Vibes", cursive;
    font-weight: 400;
    color: var(--magenta);
    line-height: 1;
    white-space: nowrap;
    text-shadow:
      3px 0 0 var(--white), -3px 0 0 var(--white),
      0 3px 0 var(--white), 0 -3px 0 var(--white),
      2px 2px 0 var(--white), -2px -2px 0 var(--white),
      2px -2px 0 var(--white), -2px 2px 0 var(--white);
  }
  .card__title--first { left: 400px; top: 40px; font-size: 150px; }
  .card__title--second { left: 500px; top: 200px; font-size: 150px; }
  .card__band {
    position: absolute;
    left: 0;
    top: 470px;
    width: 100%;
    height: 168px;
    background: var(--magenta);
    color: var(--white);
    font-family: "Roboto Condensed", "Arial Narrow", sans-serif;
    font-size: 29px;
  }
  .contact-line {
    position: absolute;
    left: 0;
    width: 100%;
    display: flex;
    justify-content: center;
    align-items: center;
    gap: 28px;
    white-space: nowrap;
  }
  .contact-line--address { top: 36px; }
  .contact-line--reach { top: 92px; }
  .contact-item { display: flex; align-items: center; gap: 10px; }
  .contact-icon { width: 34px; height: 34px; flex: none; }
</style>
</head>
<body>
  <div class="card">
    <div class="card__photo" role="img" aria-label="Photograph of a smiling woman with long curly auburn hair resting her chin on her hand, set against a soft blurred green and blue garden with pink blossoms"></div>
    <div class="card__title card__title--first">Amber</div>
    <div class="card__title card__title--second">Meadow</div>

    <div class="card__band">
      <div class="contact-line contact-line--address">
        <span class="contact-item">
          <svg class="contact-icon" viewBox="0 0 34 34" aria-hidden="true">
            <circle cx="17" cy="17" r="16" fill="#fff"/>
            <path d="M17 7a7 7 0 0 0-7 7c0 5.5 7 13 7 13s7-7.5 7-13a7 7 0 0 0-7-7z" fill="#e2007a"/>
            <circle cx="17" cy="14" r="2.8" fill="#fff"/>
          </svg>
          LLC Lydia Rose Vandermeer 427 West Orchard Lane Ste 5-384 Phoenix, AZ 85317
        </span>
      </div>
      <div class="contact-line contact-line--reach">
        <span class="contact-item">
          <svg class="contact-icon" viewBox="0 0 34 34" aria-hidden="true">
            <circle cx="17" cy="17" r="16" fill="#fff"/>
            <rect x="11.5" y="7" width="11" height="20" rx="2" fill="#e2007a"/>
            <rect x="13" y="9.5" width="8" height="13" fill="#fff"/>
            <circle cx="17" cy="24.7" r="1.1" fill="#fff"/>
          </svg>
          602-718-3054
        </span>
        <span class="contact-item">
          <svg class="contact-icon" viewBox="0 0 34 34" aria-hidden="true">
            <circle cx="17" cy="17" r="16" fill="#fff"/>
            <rect x="8" y="11" width="18" height="12" rx="1" fill="none" stroke="#e2007a" stroke-width="2"/>
            <path d="M8 11l9 7 9-7" fill="none" stroke="#e2007a" stroke-width="2"/>
          </svg>
          lvandermeer@pinemail.net
        </span>
      </div>
    </div>
  </div>
</body>
</html>
```